Velta Harbor Solutions

I have a file with a logo. It is grainy. I also have a board with my color pallet and other branding items. I need a file with the logo that is high resolution and I also need a business card design.

```html
<!DOCTYPE html>
<html lang="en">
<head>
<meta charset="utf-8">
<title>Velta Harbor Solutions – Business Card</title>
<link href="https://fonts.googleapis.com/css2?family=Montserrat:wght@400;500;700&family=Roboto:wght@400&display=swap" rel="stylesheet">
<style>
  :root {
    --backdrop: #222831;
    --navy: #232833;
    --paper: #e4e4e4;
    --ink: #1c1e22;
    --ink-soft: #2c3a52;
    --muted: #a9a9a9;
    --accent: #c0242a;
    --white: #ffffff;
  }
  * { box-sizing: border-box; margin: 0; padding: 0; }
  html, body { width: 1200px; height: 1170px; overflow: hidden; }
  body {
    background: var(--backdrop);
    font-family: "Roboto", Arial, sans-serif;
    position: relative;
  }
  .card {
    position: absolute;
    left: 220px;
    width: 760px;
    height: 434px;
    background: var(--paper);
    box-shadow: 0 24px 50px rgba(0,0,0,0.35);
    overflow: hidden;
  }
  .card--back { top: 110px; display: flex; flex-direction: column; align-items: center; justify-content: center; }
  .card--front { top: 626px; display: flex; }

  .brand-name {
    font-family: "Montserrat", Arial, sans-serif;
    font-weight: 700;
    letter-spacing: 0.06em;
    text-transform: uppercase;
    text-align: center;
    line-height: 1.15;
  }
  .card--back .brand-name { color: var(--navy); font-size: 44px; }
  .card--back .tagline {
    margin-top: 26px;
    font-family: "Montserrat", Arial, sans-serif;
    font-size: 13px;
    letter-spacing: 0.22em;
    text-transform: uppercase;
    color: var(--ink-soft);
  }
  .card--back .rule { width: 280px; height: 2px; background: var(--accent); margin-top: 22px; }

  .brand-panel {
    width: 290px;
    background: var(--navy);
    display: flex; flex-direction: column; align-items: center; justify-content: center;
    padding: 0 28px;
    position: relative;
  }
  .brand-panel .brand-name { color: var(--white); font-size: 26px; }
  .brand-panel .tagline {
    margin-top: 16px;
    font-family: "Montserrat", Arial, sans-serif;
    font-size: 10px;
    letter-spacing: 0.16em;
    text-transform: uppercase;
    color: var(--white);
    text-align: center;
    line-height: 1.6;
  }
  .details { flex: 1; position: relative; padding: 64px 0 0 58px; }
  .person-name {
    font-family: "Montserrat", Arial, sans-serif;
    font-size: 40px; color: var(--ink); font-weight: 400;
  }
  .person-name strong { font-weight: 700; }
  .person-title {
    font-family: "Montserrat", Arial, sans-serif;
    font-size: 19px; color: var(--muted); margin-top: 4px; margin-left: 40px;
  }
  .contact-list { list-style: none; margin-top: 52px; margin-left: -76px; }
  .contact-list li {
    display: flex; align-items: flex-start; gap: 22px;
    font-size: 19px; color: var(--ink-soft); line-height: 1.25;
    margin-bottom: 13px;
  }
  .icon {
    flex: none; width: 34px; height: 34px; border-radius: 50%;
    background: var(--accent);
    display: flex; align-items: center; justify-content: center;
  }
  .icon svg { width: 18px; height: 18px; }
  .contact-list span { padding-top: 5px; }
</style>
</head>
<body>

<section class="card card--back">
  <h1 class="brand-name">Velta Harbor<br>Solutions</h1>
  <div class="rule"></div>
  <p class="tagline">Low-Code Platform Development</p>
</section>

<section class="card card--front">
  <div class="brand-panel">
    <h2 class="brand-name">Velta Harbor<br>Solutions</h2>
    <p class="tagline">Low-Code Platform<br>Development</p>
  </div>
  <div class="details">
    <p class="person-name"><strong>OWEN</strong> MARSH</p>
    <p class="person-title">General Manager</p>
    <ul class="contact-list">
      <li>
        <div class="icon"><svg viewBox="0 0 24 24" fill="none" stroke="#fff" stroke-width="2" stroke-linecap="round" stroke-linejoin="round"><path d="M5 3h4l2 5-2.5 1.5a11 11 0 0 0 6 6L16 13l5 2v4a2 2 0 0 1-2 2A16 16 0 0 1 3 5a2 2 0 0 1 2-2z"/></svg></div>
        <span>+0201555010294</span>
      </li>
      <li>
        <div class="icon"><svg viewBox="0 0 24 24" fill="none" stroke="#fff" stroke-width="2" stroke-linejoin="round"><rect x="3" y="6" width="18" height="12" rx="1"/><path d="M3 7l9 6 9-6"/></svg></div>
        <span>info@veltaharbor.com</span>
      </li>
      <li>
        <div class="icon"><svg viewBox="0 0 24 24" fill="none" stroke="#fff" stroke-width="1.8"><circle cx="12" cy="12" r="9"/><ellipse cx="12" cy="12" rx="4" ry="9"/><path d="M3 12h18M5 7h14M5 17h14"/></svg></div>
        <span>www.veltaharbor.com</span>
      </li>
      <li>
        <div class="icon"><svg viewBox="0 0 24 24" fill="#fff"><path d="M12 2a7 7 0 0 0-7 7c0 5 7 13 7 13s7-8 7-13a7 7 0 0 0-7-7zm0 9.5A2.5 2.5 0 1 1 12 6.5a2.5 2.5 0 0 1 0 5z"/></svg></div>
        <span>18 Linden St, Brooklyn,<br>New York 11206, USA.</span>
      </li>
    </ul>
  </div>
</section>

</body>
</html>
```